Brochure for a paper wholesaler who wants to educate his print industry clients

We will be making a stapled informative brochure, that contains basic information about our paper products - the types of paper there is, their characteristics and other useful information.
As we are part of a paper wholesaler group in Europe - VORENT, we received a brochure in German that has this kind of information. The text in it is not as important. What is important is the layout of the document and how the text will appear in it (added in the uploaded files - 210915_Wiessenswertes_TBLK_F51.pdf).
We are allowed to tinker with this file and adjust it to our needs. So there are also .idml and .indd files available (also in the uploaded files).
We would like to keep the custom page size of 210 x290mm (8.3x11.4 in), or you can go up to 210x297mm (8.3x11.7 in).
What we want is a modern looking design that contains our companies red bordo and white/ grey colours to replace the existing green colours in this borchure. The pictures and appearance of the file can be changed according to your views and what you think would look good. We don't necessarily want to keep the same design, we just want the layout of the document be the same, as we will be placing our translated text into it. The VORENT logo should be replaced with our own logo (KUMET Logo.png).
As for how it could look, it could go together with our paper presentation, for which the design can be seen in the "KUMET Base - v2.pptx".
Holiday season, so have a lot of tasks to take care of and not as much time to check ArtHarbor as often.

```html
<!DOCTYPE html>
<html lang="en">
<head>
<meta charset="utf-8">
<title>Worth Knowing – Paper and Cardboard Guide</title>
<link rel="stylesheet" href="https://fonts.googleapis.com/css2?family=Montserrat:wght@400;600;700;800&family=Raleway:wght@300;400;600&family=Roboto+Condensed:wght@300;400;700&display=swap">
<style>
:root{
  --bordo:#7a2a31;
  --bordo-dark:#5a1c22;
  --bordo-light:#a5414b;
  --grey:#e8e8ec;
  --grey-mid:#c9c9cf;
  --ink:#2b2b2f;
  --muted:#8a8a92;
  --white:#ffffff;
  --stage:#f4f4f5;
}
*{margin:0;padding:0;box-sizing:border-box}
html,body{width:1200px;height:2938px;overflow:hidden;background:var(--stage);font-family:"Raleway",sans-serif;color:var(--ink)}
.page{position:absolute;background:var(--white);overflow:hidden;box-shadow:0 6px 24px rgba(0,0,0,.12)}
.brand{position:absolute;display:flex;align-items:center;gap:8px;font-family:"Montserrat",sans-serif;font-weight:600;letter-spacing:6px;font-size:11px;color:var(--bordo)}
.brand .mark{width:12px;height:12px;border:2px solid var(--bordo)}
.footer-bar{position:absolute;height:8px;background:var(--grey)}
.footer-tab{position:absolute;width:16px;height:12px;background:var(--bordo)}

/* cover */
.cover{left:325px;top:40px;width:500px;height:725px;background:var(--bordo)}
.cover-photo{position:absolute;left:0;top:0;width:500px;height:500px;background:linear-gradient(125deg,var(--bordo) 0%,#3a2a2e 30%,#e9e7ea 55%,#c9c6cb 75%,#232326 100%)}
.cover-brand{position:absolute;right:20px;top:18px;font-family:"Montserrat",sans-serif;font-weight:600;font-size:13px;letter-spacing:4px;color:var(--white)}
.cover-title{position:absolute;left:27px;top:520px;color:var(--white)}
.cover-title h1{font-family:"Montserrat",sans-serif;font-weight:700;font-size:22px;letter-spacing:1px}
.cover-title h2{font-family:"Raleway",sans-serif;font-weight:300;font-size:18px;letter-spacing:4px;line-height:21px;margin-top:6px}
.cover-title hr{border:0;border-top:1px solid rgba(255,255,255,.8);width:305px;margin:10px 0 6px}
.cover-title p{font-size:14px;font-weight:300}

/* toc */
.toc{left:40px;top:835px;width:465px;height:700px;background:#f3f3f5}
.toc-head{position:absolute;left:118px;top:235px;font-family:"Montserrat",sans-serif;font-size:18px;color:var(--bordo-dark)}
.toc-head b{display:block;font-weight:700;color:var(--bordo)}
.toc-head span{display:block;width:48px;height:3px;background:var(--bordo);margin-top:6px}
.toc-box{position:absolute;left:75px;top:330px;width:245px;height:320px;background:linear-gradient(160deg,var(--bordo-light),var(--bordo-dark))}
.toc-box hr{position:absolute;left:40px;top:38px;width:155px;border:0;border-top:2px solid var(--white)}
.toc-list{position:absolute;left:40px;top:85px;width:180px;list-style:none;color:var(--white);font-family:"Montserrat",sans-serif;font-size:8px}
.toc-list li{display:flex;justify-content:space-between;margin-bottom:14px}
.toc-side{position:absolute;left:330px;top:360px;writing-mode:vertical-rl;transform:rotate(180deg);font-family:"Montserrat",sans-serif;font-weight:800;font-size:38px;letter-spacing:2px;color:#d4d2de}

/* technical terms */
.terms{left:505px;top:835px;width:465px;height:700px}
.terms h3{position:absolute;left:30px;top:32px;font-family:"Roboto Condensed",sans-serif;font-weight:300;font-size:15px;color:var(--muted);line-height:17px}
.terms h3 b{display:block;font-weight:400;color:var(--bordo)}
.terms .lead{position:absolute;left:30px;top:78px;font-family:"Roboto Condensed",sans-serif;font-size:9px}
.def-list{position:absolute;left:30px;top:106px;width:410px;font-family:"Roboto Condensed",sans-serif;font-size:8px;color:var(--muted)}
.def-list div{display:grid;grid-template-columns:80px 1fr;margin-bottom:17px}
.def-list dt{color:var(--ink)}
.abbr-title{position:absolute;left:30px;top:300px;font-family:"Roboto Condensed",sans-serif;font-size:8px}
.abbr{position:absolute;left:30px;top:325px;width:410px;border-collapse:collapse;font-family:"Roboto Condensed",sans-serif;font-size:8px;color:var(--muted)}
.abbr td{height:24px;padding:0 6px}
.abbr td:first-child{background:var(--bordo);color:var(--white);width:34px;font-weight:700}
.abbr td:nth-child(2){width:110px}

/* about us */
.about{left:40px;top:1700px;width:560px;height:960px}
.about-photo{position:absolute;left:0;top:0;width:560px;height:270px;background:linear-gradient(150deg,#9a5058,#7d3038 55%,#a87a7e)}
.about h3{position:absolute;left:52px;top:100px;font-family:"Montserrat",sans-serif;font-weight:600;font-size:24px;color:var(--white)}
.steps{position:absolute;left:30px;top:198px;width:500px;display:flex;justify-content:space-between}
.step{width:96px;text-align:center;font-family:"Montserrat",sans-serif}
.step .num{color:var(--white);font-weight:600;font-size:15px;height:30px}
.step .icon{margin:0 auto;width:38px;height:42px;background:var(--white);clip-path:polygon(0 20%,50% 0,100% 20%,100% 100%,0 100%);display:flex;align-items:center;justify-content:center}
.step .icon i{width:16px;height:16px;border:2px solid var(--bordo);border-radius:50%}
.step .val{font-weight:700;font-size:10px;margin-top:22px;color:var(--ink);white-space:nowrap}
.step .lab{font-family:"Raleway",sans-serif;font-size:9px;color:var(--muted);margin-top:8px;line-height:11px}
.arrow{position:absolute;top:244px;color:var(--ink);font-size:14px}
.logistics{position:absolute;left:52px;top:430px;font-family:"Montserrat",sans-serif;font-weight:800;font-size:20px;letter-spacing:3px;color:var(--bordo);line-height:22px}
.route{position:absolute;left:0;top:490px;width:560px;height:420px;background:linear-gradient(160deg,#f6f6f8 0%,#ececef 45%,#d9b9bd 75%,var(--bordo) 100%)}
.milestone{position:absolute;font-family:"Montserrat",sans-serif;font-size:12px;font-weight:700;color:var(--ink);line-height:14px}
.milestone small{display:block;font-family:"Raleway",sans-serif;font-weight:400;color:#5e5e66;font-size:10px;line-height:12px;margin-top:2px}

/* format details */
.details{left:600px;top:1700px;width:560px;height:960px}
.details h3{position:absolute;left:20px;top:40px;font-family:"Roboto Condensed",sans-serif;font-size:26px;font-weight:400;color:var(--bordo)}
.spec{position:absolute;left:20px;top:95px;width:520px;border-collapse:collapse;font-family:"Roboto Condensed",sans-serif;font-size:10px;text-align:center}
.spec th{background:var(--bordo);color:var(--white);font-weight:400;padding:5px 4px;line-height:11px}
.spec td{padding:6px 4px;border-bottom:1px solid var(--grey);line-height:12px;vertical-align:middle}
.spec td:first-child{font-size:8px;color:var(--muted);width:44px}
.spec td:nth-child(2){font-size:9px}
.spec tr:nth-child(even) td{background:#f6f6f8}
.fmt-title{position:absolute;left:20px;top:510px;font-family:"Roboto Condensed",sans-serif;font-weight:300;font-size:24px}
.fmt-title b{font-weight:700;color:var(--bordo)}
.fmt-sub{position:absolute;left:20px;top:560px;font-family:"Roboto Condensed",sans-serif;font-size:8px;font-weight:700}
.fmt-text{position:absolute;left:20px;top:580px;width:500px;font-family:"Roboto Condensed",sans-serif;font-size:9px;color:var(--muted);line-height:12px}
.fmt-list{position:absolute;left:80px;top:660px;font-family:"Roboto Condensed",sans-serif;font-size:10px}
.fmt-list h4{font-size:10px;margin-bottom:10px}
.fmt-list div{display:grid;grid-template-columns:40px 120px;margin-bottom:10px}
.fmt-note{position:absolute;left:80px;top:905px;font-family:"Roboto Condensed",sans-serif;font-size:9px}
</style>
</head>
<body>

<section class="page cover">
  <div class="cover-photo" role="img" aria-label="Photograph of fanned paper sheets"></div>
  <div class="cover-brand">KUMET</div>
  <div class="cover-title">
    <h1>WORTH KNOWING!</h1>
    <h2>FORMATS, CLASSES,<br>COLORS, CALCULATIONS</h2>
    <hr>
    <p>Guide for handling paper and cardboard</p>
  </div>
</section>

<section class="page toc">
  <div class="toc-head">Table<b>of Content</b><span></span></div>
  <div class="toc-box">
    <hr>
    <ol class="toc-list">
      <li><span>1. Welcome &amp; Content</span><span>02</span></li>
      <li><span>2. Overview &amp; Services</span><span>04</span></li>
      <li><span>3. Our Team &amp; Skills</span><span>06</span></li>
      <li><span>4. Work Process &amp; Fcts</span><span>08</span></li>
      <li><span>5. Projects &amp; Reviews</span><span>10</span></li>
      <li><span>6. Portfolio &amp; Case Study</span><span>12</span></li>
      <li><span>7. Future Plan &amp; Statistics</span><span>14</span></li>
    </ol>
  </div>
  <div class="toc-side">PROPOSAL</div>
  <div class="brand" style="left:75px;top:665px"><span class="mark"></span>KUMET</div>
  <div class="footer-bar" style="left:165px;top:668px;width:280px"></div>
  <div class="footer-tab" style="left:420px;top:666px"></div>
</section>

<section class="page terms">
  <h3>Technical<b>Terms</b></h3>
  <p class="lead">Most common technical terms and abbreviations</p>
  <dl class="def-list">
    <div><dt>Uncoated</dt><dd>Unrefined, machine-smooth or satin papers made from various fiber materials can be produced</dd></div>
    <div><dt>Coated papers</dt><dd>Unrefined, machine-smooth or satin papers made from various fiber materials can be produced</dd></div>
    <div><dt>Cardboards</dt><dd>Unrefined, machine-smooth or satin papers made from various fiber materials can be produced</dd></div>
    <div><dt>Fiber boards</dt><dd>Unrefined, machine-smooth or satin papers made from various fiber materials can be produced</dd></div>
    <div><dt>Special papers</dt><dd>Unrefined, machine-smooth or satin papers made from various fiber materials can be produced</dd></div>
  </dl>
  <p class="abbr-title">Abbreviations and their translation</p>
  <table class="abbr">
    <tr><td>WFU</td><td>woodfree, uncoated</td><td>Unrefined, machine-smooth or satin papers</td></tr>
    <tr><td>MFS</td><td>machine-finished special</td><td>Unrefined, machine-smooth or satin papers</td></tr>
    <tr><td>WF</td><td>woodfree</td><td>Unrefined, machine-smooth or satin papers</td></tr>
    <tr><td>MWC</td><td>middleweight, coated</td><td>Unrefined, machine-smooth or satin papers</td></tr>
    <tr><td>LWC</td><td>lightweight, coated</td><td>Unrefined, machine-smooth or satin papers</td></tr>
    <tr><td>ULWC</td><td>ultralightweight, coated</td><td>Unrefined, machine-smooth or satin papers</td></tr>
    <tr><td>MF</td><td>machine-finished</td><td>Unrefined, machine-smooth or satin papers</td></tr>
    <tr><td>SC-A</td><td>supercalendered</td><td>Unrefined, machine-smooth or satin papers</td></tr>
    <tr><td>SC-B</td><td>supercalendered</td><td>Unrefined, machine-smooth or satin papers</td></tr>
    <tr><td>SCO</td><td>softcalendered</td><td>Unrefined, machine-smooth or satin papers</td></tr>
    <tr><td>FCO</td><td>film coated offset</td><td>Unrefined, machine-smooth or satin papers</td></tr>
    <tr><td>HSWO</td><td>heatset web offset</td><td>Unrefined, machine-smooth or satin papers</td></tr>
  </table>
  <div class="brand" style="left:30px;top:665px;font-size:8px;letter-spacing:4px"><span class="mark" style="width:9px;height:9px"></span>KUMET</div>
  <div class="footer-bar" style="left:110px;top:668px;width:320px"></div>
  <div class="footer-tab" style="left:420px;top:666px"></div>
</section>

<section class="page about">
  <div class="about-photo" role="img" aria-label="Photograph of stacked paper sheets tinted in bordo"></div>
  <h3>About Us</h3>
  <div class="steps">
    <div class="step"><div class="num">01</div><div class="icon"><i></i></div><div class="val">1993</div><div class="lab">ANNO</div></div>
    <div class="step"><div class="num">02</div><div class="icon"><i></i></div><div class="val">1700+</div><div class="lab">Active Costumer</div></div>
    <div class="step"><div class="num">03</div><div class="icon"><i></i></div><div class="val">over 10000</div><div class="lab">Assortment Positions</div></div>
    <div class="step"><div class="num">04</div><div class="icon"><i></i></div><div class="val">ONE-STOP-SHOP</div><div class="lab">Everything for Printing in One Place</div></div>
    <div class="step"><div class="num">05</div><div class="icon"><i></i></div><div class="val">34 (2023)</div><div class="lab">Employees</div></div>
  </div>
  <span class="arrow" style="left:134px">→</span>
  <span class="arrow" style="left:235px">→</span>
  <span class="arrow" style="left:336px">→</span>
  <span class="arrow" style="left:437px">→</span>
  <div class="logistics">KUMET<br>Logistics</div>
  <div class="route" role="img" aria-label="Illustration of a delivery route climbing toward mountain peaks with a paper plane"></div>
  <div class="milestone" style="left:110px;top:820px">6000+ m2<small>Our own Logistic Center</small></div>
  <div class="milestone" style="left:180px;top:750px">12000+<small>Pallet spaces in our<br>combined warehouses</small></div>
  <div class="milestone" style="left:260px;top:690px">24H<small>Delivery in Latvia</small></div>
  <div class="milestone" style="left:320px;top:630px">up to 38<small>Incoming cargo trucks per month</small></div>
  <div class="milestone" style="left:400px;top:575px">8<small>Our own delivery Trucks</small></div>
  <div class="milestone" style="left:430px;top:515px">at least 20<small>Delivery trips per day</small></div>
  <div class="brand" style="left:52px;top:925px"><span class="mark"></span>KUMET</div>
</section>

<section class="page details">
  <h3>Format Details</h3>
  <table class="spec">
    <tr><th></th><th>Strich</th><th>Bekannte Bezeichnung</th><th>Kurz-bezeichnung</th><th>Englische Bezeichnung</th></tr>
    <tr><td>Gebleicht, weiß, gestrichen</td><td>Einseitig oder zweiseitig zweifach gestrichen</td><td>Sulfatkarton= Zellstoffkarton</td><td>GZ, gestrichener Zellstoffkarton</td><td>SBS board, Solid Bleached Sulfat Board</td></tr>
    <tr><td>Ungebleicht, braun, gestrichen</td><td>Einseitig oder zweiseitig gestrichen</td><td>Kraftkarton</td><td>GN 4, gestrichener, ungebleichter Zellstoffkarton mit brauner Rückseite</td><td>CNK, Coated Natural Kraft SUB, Solid Unbleached Board</td></tr>
    <tr><td>Gestrichen, weiße Rückseite</td><td>Einfach gestrichene Rückseite, Vorderseite zweifach gestrichen</td><td>Faltschachtel-karton</td><td>GC 1, gestrichener Chromokarton</td><td>FBB, Folding Box Board coated 1 side</td></tr>
    <tr><td>Ungestrichen, heller Rückseite</td><td>Helle, ungestrichene Rückseite, Vorderseite zweifach gestrichen</td><td>Faltschachtel-karton</td><td>GC 2, gestrichener Chromokarton 2</td><td>FBB, Folding Box Board with manilla back</td></tr>
    <tr><td>Mit grauer Rückseite</td><td>Rückseite pigmentiert, Vorderseite zweifach gestrichen</td><td>Duplexkarton</td><td>GD 2, gestrichener Duplexkarton 2</td><td>WLC, White Lined Chipboard</td></tr>
  </table>
  <div class="fmt-title">The small 1x1 of the <b>format</b></div>
  <div class="fmt-sub">DIN and ISO Lagerformate</div>
  <p class="fmt-text">Paper sizes are standardized according to DIN. The original format of series A is a rectangle measuring 1 square meter. Each additional format is obtained by halving or doubling and has an aspect ratio of 1:√2. From the additional DIN series B, C and D come the raw formats, which match the DIN A series, are also common formats.</p>
  <div class="fmt-list">
    <h4>DIN-B-Formate</h4>
    <div><span>B0</span><span>1.000 x 1.414 mm</span></div>
    <div><span>B1</span><span>707 x 1.000 mm</span></div>
    <div><span>B2</span><span>500 x 707 mm</span></div>
    <div><span>B3</span><span>353 x 500 mm</span></div>
    <div><span>*B4</span><span>250 x 353 mm</span></div>
    <div><span>*B5</span><span>176 x 250 mm</span></div>
    <div><span>*B6</span><span>125 x 176 mm</span></div>
    <div><span>B7</span><span>88 x 125 mm</span></div>
  </div>
  <p class="fmt-note">*Briefhüllen-/Versandtaschenformat</p>
  <div class="footer-bar" style="left:80px;top:935px;width:420px"></div>
  <div class="footer-tab" style="left:520px;top:933px"></div>
</section>

</body>
</html>
```